Valu Tea Label & packaging for a premium tea brand. For local and global market

Create a look and feel for a box and rectangle tin. We are looking for a luxe packaging design for a new tea brand based in Kenya called 'Valu Tea'. Kenya is home to the finest teas in the world and Valu tea looks to embody that fact. Valu Tea uses the most premium of Kenyan Tea, Black tea, Purple tea, White Tea, Green tea, Hibiscus Tea and Moringa Tea. Valu Tea is handpicked from Kenya's highlands. This project will include the look and feel of the different teas described above. The copy on the main face of the box should read 'Premium Kenyan Tea' The box will contain 25 tagged tea bags, with a net weight of 50 gms.

On one side of the box will read 'packaging instructions' To fully savour this Valu premium tea, use one tea bag for each cup, add some freshly bolded water and wait for 2 minutes as you enjoy the sweet aroma of our tea, stir and serve' Ingredients : Black Tea, and for the others the same : Hibiscus Tea, Green Tea, Purple Tea, White tea. should also feature on the label: Produce of Kenya.

Target Market(s)

Premium

Industry/Entity Type

Agribusiness

Font styles to use
Script

Colors

Designer to choose colors to be used in the design.

Requirements
Must have
• Luxe look and feel
Nice to have
• I have attached the Valu tea logo and images of brands I'd lile the designer to be inspired by.
Should not have
• Green and yellow colours

```html
<!DOCTYPE html>
<html lang="en">
<head>
<meta charset="utf-8">
<title>Valu Tea – Purple Tea Tin</title>
<link rel="stylesheet" href="https://fonts.googleapis.com/css2?family=Libre+Baskerville:ital,wght@0,400;1,400&family=Roboto+Condensed:wght@300&display=swap">
<style>
  :root {
    --backdrop: #a9acb1;
    --tin-black: #1d1a1b;
    --lid-black: #221e20;
    --lid-rim: #2a2527;
    --gold-line: #b39a6e;
    --bronze: #9b6a3d;
    --pattern-dark: #2a211c;
    --pattern-mid: #4a3526;
    --label-plum: #3b0a2a;
    --copper: #d98c6c;
    --ivory: #f4efe9;
    --muted-lilac: #b7a5ae;
  }
  * { margin: 0; padding: 0; box-sizing: border-box; }
  html, body { width: 1200px; height: 639px; overflow: hidden; }
  body { background: var(--backdrop); position: relative; }

  .tin { position: absolute; left: 382px; top: 74px; width: 452px; height: 520px; }

  .tin-lid {
    position: absolute; left: -6px; top: 0; width: 464px; height: 58px;
    background: var(--lid-black);
    border-radius: 10px 10px 2px 2px;
    border-bottom: 4px solid var(--lid-rim);
  }
  .tin-seam {
    position: absolute; left: -6px; top: 58px; width: 464px; height: 3px;
    background: var(--gold-line);
  }
  .tin-body {
    position: absolute; left: 0; top: 61px; width: 452px; height: 459px;
    background: var(--tin-black);
    border-radius: 0 0 6px 6px;
  }
  .pattern-band {
    position: absolute; left: 0; top: 6px; width: 452px; height: 352px;
    background: linear-gradient(135deg, var(--pattern-mid), var(--pattern-dark) 55%, var(--pattern-mid));
  }

  .label-frame {
    position: absolute; left: 96px; top: 119px; width: 262px; height: 287px;
    background: var(--tin-black);
    border: 2px solid var(--bronze);
    padding: 8px;
  }
  .label-panel {
    width: 100%; height: 100%;
    background: var(--label-plum);
    border: 2px solid var(--bronze);
    text-align: center;
    color: var(--ivory);
    position: relative;
  }
  .brand-name {
    position: absolute; left: 0; right: 0; top: 70px;
    font-family: "Libre Baskerville", Georgia, serif;
    font-weight: 400;
    font-size: 46px;
    letter-spacing: 3px;
    color: var(--copper);
  }
  .tea-name {
    position: absolute; left: 0; right: 0; top: 132px;
    font-family: "Libre Baskerville", Georgia, serif;
    font-size: 22px;
    letter-spacing: 1.5px;
    color: var(--ivory);
  }
  .tea-mood {
    position: absolute; left: 0; right: 0; top: 162px;
    font-family: "Libre Baskerville", Georgia, serif;
    font-style: italic;
    font-size: 16px;
    letter-spacing: 0.5px;
    color: var(--muted-lilac);
  }
  .net-contents {
    position: absolute; left: 0; right: 0; top: 227px;
    font-family: "Roboto Condensed", Arial, sans-serif;
    font-weight: 300;
    font-size: 13px;
    letter-spacing: 1px;
    color: var(--ivory);
  }
</style>
</head>
<body>
  <div class="tin">
    <div class="tin-lid"></div>
    <div class="tin-seam"></div>
    <div class="tin-body">
      <div class="pattern-band" role="img" aria-label="Bronze geometric lattice pattern of diamonds and quatrefoils on black"></div>
      <div class="label-frame">
        <div class="label-panel">
          <div class="brand-name">VALU</div>
          <div class="tea-name">PURPLE TEA</div>
          <div class="tea-mood">Bold &amp; Uplifting</div>
          <div class="net-contents">25 BAGS , 50g</div>
        </div>
      </div>
    </div>
  </div>
</body>
</html>
```